Self-Serve Brazilian Buffet and BBQ sold by the pound needs a business card

For CEO -Lucia Fernanda Moura Blake
Owner/President - Marco Tiago Moura

Target Market(s)

Customers and

Industry/Entity Type

Business

Contact Information for Business Card

Lucia Fernanda Pinto Moura Blake
CEO of Terra Sol Churrasco
Brazilian BBQ Buffet sold by the pound

Requirements
Must have
• 5218 West Orchard Ave.
• Ste. K
• Santa Ana, CA 92781
• Phone : 714382-0157
• terrasolchurrasco@mailbox-example.com

```html
<!DOCTYPE html>
<html lang="en">
<head>
<meta charset="utf-8">
<title>Terra Sol Churrasco – Business Card</title>
<link rel="stylesheet" href="https://fonts.googleapis.com/css2?family=Archivo+Narrow:wght@400;500&family=Bungee&display=swap">
<style>
  :root {
    --page-bg: #e9e6e1;
    --card-black: #0b0b0b;
    --band-grey: #c9c9cb;
    --accent-red: #d8432c;
    --photo-green: #6f9a2c;
    --photo-yellow: #d9b33a;
    --photo-brown: #8a4a2a;
  }
  html, body {
    margin: 0;
    width: 1200px;
    height: 892px;
    overflow: hidden;
    background: var(--page-bg);
  }
  .canvas {
    position: relative;
    width: 1200px;
    height: 892px;
  }
  .card {
    position: absolute;
    left: 250px;
    width: 700px;
    height: 400px;
    background: var(--card-black);
    overflow: hidden;
    box-shadow: 0 6px 18px rgba(0,0,0,0.25);
  }
  .card--front { top: 30px; }
  .card--back  { top: 462px; }

  /* Front */
  .front__identity {
    position: absolute;
    left: 48px;
    top: 70px;
    color: var(--accent-red);
    font-family: "Archivo Narrow", sans-serif;
  }
  .front__name {
    margin: 0;
    font-size: 40px;
    font-weight: 500;
    letter-spacing: 0.5px;
  }
  .front__title {
    margin: 4px 0 0 70px;
    font-size: 19px;
  }
  .front__contact {
    position: absolute;
    left: 150px;
    top: 210px;
    margin: 0;
    color: var(--accent-red);
    font-family: "Archivo Narrow", sans-serif;
    font-size: 21px;
    line-height: 1.32;
    font-style: normal;
  }
  .front__photo {
    position: absolute;
    right: 0;
    top: 0;
    width: 190px;
    height: 400px;
    background: linear-gradient(160deg, var(--photo-yellow) 0%, var(--photo-green) 35%, #b5a36a 55%, var(--photo-brown) 80%, #5c3a22 100%);
  }

  /* Back */
  .back__band {
    position: absolute;
    left: 0;
    top: 0;
    width: 700px;
    height: 170px;
    background: linear-gradient(180deg, #d4d4d6, var(--band-grey));
    color: var(--accent-red);
    font-family: "Bungee", sans-serif;
    text-align: center;
  }
  .back__kicker {
    margin: 38px 0 6px;
    font-size: 30px;
    letter-spacing: 1px;
  }
  .back__tagline {
    margin: 0;
    font-size: 38px;
    letter-spacing: 1px;
  }
</style>
</head>
<body>
<main class="canvas">
  <section class="card card--front" aria-label="Business card front">
    <div class="front__identity">
      <h1 class="front__name">Marco Tiago Moura</h1>
      <p class="front__title">Owner/President</p>
    </div>
    <address class="front__contact">
      714382-0157<br>
      terrasolchurrasco@mailbox-example.com<br>
      5218 West Orchard Ave. Ste. K<br>
      Santa Ana, CA 92781
    </address>
    <div class="front__photo" role="img" aria-label="Collage of Brazilian buffet dishes: grilled meats, greens, fried plantains and side bowls"></div>
  </section>

  <section class="card card--back" aria-label="Business card back">
    <div class="back__band">
      <p class="back__kicker">Self-Serve</p>
      <p class="back__tagline">Brazilian Buffet and BBQ</p>
    </div>
  </section>
</main>
</body>
</html>
```